Design Product Packaging For Face Mask Brand

We need packaging designed for a new product, "Harbor Bloom Cover" a made in canada multi layer poly cotton reusable non-medical face mask for all people. The mask ties in the back behind the head.

Preference is a 4x6' flat polybag or 5x7" resealable stand up bag.

We would like to see bold easy to read colour block designs that use the colour pink. The final design should communicate a simple, high fashion, bold fun quality product.

IMG-9732 and 9733 are of the actual product.
Img_9695 and 9786 are our logos.
Vintageladyshoppinggreenmask is an image on our website.
2020-04_VK is the style of image we would like to have on the front of the packaging.
Maskonworldoff is an example of fun cute wording.

Please leave space for upc on the back of the package aswell. Open to your creativity in terms of design but colors must stay the same as brand.

Thank you all for you time and submissions.

Harbor Bloom Cover xoxo

Target Market(s)

Canada/USA civilians, non-health workers

Industry/Entity Type

Fashion

Font styles to use
Sans Serif

Colors
ffffff
feeeee
f9d9e8
eea4c8
e667a6
e34298
86cfc6
33b8a4
87cfc6

Requirements
Must have
• our logo, brand colors, upc on back
Nice to have
• Bold Font
Should not have
• Hard to read handwriting

```html
<!DOCTYPE html>
<html lang="en">
<head>
<meta charset="utf-8">
<title>Harbor Bloom Cover – Pouch Front</title>
<link rel="stylesheet" href="https://fonts.googleapis.com/css2?family=Anton&family=Oswald:wght@600&display=swap">
<style>
  :root {
    --backdrop: #f9a7ac;
    --pouch-pink: #dc6270;
    --pouch-pink-deep: #cf5664;
    --seal-line: #e7838e;
    --teal: #17a596;
    --teal-deep: #128b7f;
    --mask-fill: #f3c8d6;
    --white: #ffffff;
  }
  html, body {
    margin: 0;
    padding: 0;
    width: 1200px;
    height: 1158px;
    overflow: hidden;
    background: var(--backdrop);
  }
  .canvas {
    display: block;
    width: 1200px;
    height: 1158px;
  }
  .pouch-body { fill: var(--pouch-pink); }
  .pouch-seal { fill: var(--pouch-pink-deep); }
  .zip-line { stroke: var(--seal-line); stroke-width: 2; fill: none; }
  .colour-band { fill: var(--teal); }
  .bottom-seal { fill: var(--teal-deep); }
  .brand-name {
    font-family: "Oswald", sans-serif;
    font-weight: 600;
    fill: var(--white);
  }
  .brand-dot { fill: var(--white); }
  .headline {
    font-family: "Anton", sans-serif;
    font-size: 80px;
    fill: var(--white);
  }
  .headline-shadow {
    font-family: "Anton", sans-serif;
    font-size: 80px;
    fill: var(--pouch-pink);
  }
  .product-art { fill: var(--mask-fill); }
</style>
</head>
<body>
<svg class="canvas" viewBox="0 0 1200 1158" xmlns="http://www.w3.org/2000/svg">
  <g class="pouch" transform="translate(323 233)">
    <!-- bag shape -->
    <rect class="pouch-body" x="0" y="0" width="525" height="713" rx="12"/>
    <rect class="pouch-seal" x="0" y="0" width="525" height="60" rx="12"/>
    <line class="zip-line" x1="28" y1="67" x2="497" y2="67"/>
    <line class="zip-line" x1="28" y1="74" x2="497" y2="74"/>

    <!-- colour blocks -->
    <polygon class="colour-band" points="0,373 525,248 525,425 0,483"/>
    <polygon class="colour-band" points="0,686 525,598 525,713 0,713"/>
    <rect class="bottom-seal" x="0" y="698" width="525" height="15" rx="6"/>

    <!-- brand mark -->
    <g class="brand-lockup">
      <circle class="brand-dot" cx="262" cy="166" r="18"/>
      <text class="brand-name" x="262" y="218" font-size="22" text-anchor="middle">HARBOR BLOOM COVER</text>
    </g>

    <!-- headline -->
    <g class="headline-group" transform="translate(70 356) rotate(-8) skewX(-12)">
      <g aria-hidden="true">
        <text class="headline-shadow" x="5" y="5" textLength="400" lengthAdjust="spacingAndGlyphs">GET A MASK,</text>
        <text class="headline-shadow" x="-7" y="93" textLength="430" lengthAdjust="spacingAndGlyphs">GIVE A MASK</text>
      </g>
      <text class="headline" x="0" y="0" textLength="400" lengthAdjust="spacingAndGlyphs">GET A MASK,</text>
      <text class="headline" x="-12" y="88" textLength="430" lengthAdjust="spacingAndGlyphs">GIVE A MASK</text>
    </g>

    <!-- product image area -->
    <path class="product-art" role="img" aria-label="Pink pleated reusable face mask with white ear loops"
          d="M57 560 Q60 522 110 505 L220 486 Q290 470 292 500 L286 640 Q270 672 150 668 L75 650 Q55 640 57 600 Z"/>

    <!-- name badge -->
    <g class="name-badge">
      <text class="brand-name" x="400" y="630" font-size="24" text-anchor="middle">HARBOR</text>
      <text class="brand-name" x="400" y="658" font-size="24" text-anchor="middle">BLOOM</text>
      <text class="brand-name" x="400" y="686" font-size="24" text-anchor="middle">COVER</text>
    </g>
  </g>
</svg>
</body>
</html>
```